Business Card Design for Marketing Firm

Looking for business card design for higher end marketing firm. Clean but impressionable/trendy. We are a marketing firm that represents manufacturers in the foodservice equipment and supply industry. Our customers are end users such has hotels, restaurants, country clubs, convention centers and casinos as well as distributors of restaurants supplies and equipment, and manufacturers of foodservice equipment and supplies.
Target Market(s)
Hotels, Restaurants, Supply & Equipment Distributors, Foodservice Manufacturers
Industry/Entity Type
Foodservice/Hospitality
Contact Information for Business Card
Name, Title, Contact Number, Email, Website, Social Media, Address
Requirements
Must have
- Clean & Simple but Serious and Impressionable

```html
<!DOCTYPE html>
<html lang="en">
<head>
<meta charset="utf-8">
<title>Meridian Hospitality Reps – Business Card</title>
<link href="https://fonts.googleapis.com/css2?family=Figtree:wght@500;700&display=swap" rel="stylesheet">
<style>
  :root {
    --backdrop: #969696;
    --navy: #02007c;
    --white: #ffffff;
  }
  * { margin: 0; padding: 0; box-sizing: border-box; }
  html, body {
    width: 1200px;
    height: 1200px;
    overflow: hidden;
    background: var(--backdrop);
    font-family: "Figtree", Arial, sans-serif;
  }
  .card {
    position: absolute;
    width: 797px;
    height: 466px;
  }
  .card-front {
    left: 201px;
    top: 84px;
    background: var(--white);
    display: flex;
    align-items: center;
    justify-content: center;
  }
  .front-brand {
    color: var(--navy);
    font-weight: 700;
    font-size: 64px;
    line-height: 1.05;
    letter-spacing: 2px;
    text-align: center;
    text-transform: uppercase;
  }
  .card-back {
    left: 200px;
    top: 600px;
    background: var(--navy);
    color: var(--white);
  }
  .brand-block {
    position: absolute;
    left: 86px;
    top: 200px;
    width: 262px;
    text-align: center;
  }
  .brand-name {
    font-weight: 500;
    font-size: 24px;
    letter-spacing: 1px;
    text-transform: uppercase;
    line-height: 1.1;
  }
  .brand-rule {
    height: 1px;
    background: var(--white);
    margin: 8px 0 0;
  }
  .social {
    display: flex;
    justify-content: center;
    gap: 7px;
    margin-top: 28px;
  }
  .social-dot {
    width: 34px;
    height: 34px;
    border-radius: 50%;
    background: var(--white);
  }
  .divider {
    position: absolute;
    left: 398px;
    top: 130px;
    width: 1px;
    height: 206px;
    background: var(--white);
  }
  .contact {
    position: absolute;
    left: 438px;
    top: 126px;
    font-size: 20px;
    font-weight: 500;
    line-height: 27px;
    list-style: none;
  }
  .contact .person-name { font-weight: 700; }
  .contact .gap { margin-top: 27px; }
</style>
</head>
<body>
  <section class="card card-front">
    <p class="front-brand">Meridian<br>Hospitality Reps</p>
  </section>

  <section class="card card-back">
    <div class="brand-block">
      <p class="brand-name">Meridian Hospitality Reps</p>
      <div class="brand-rule"></div>
      <div class="social">
        <span class="social-dot" aria-label="Social profile"></span>
        <span class="social-dot" aria-label="Social profile"></span>
      </div>
    </div>
    <div class="divider"></div>
    <ul class="contact">
      <li class="person-name">Name Surname</li>
      <li>Title</li>
      <li class="gap">123 456 7890</li>
      <li>name@meridianhospitalityreps.com</li>
      <li>meridianhospitalityreps.com</li>
      <li class="gap">Brookfield, Texas</li>
    </ul>
  </section>
</body>
</html>
```